Corporate Christmas Card Email Template Design

We need a Corporate Christmas Card Design to Email all our customers with our Corporate Logos in it.

Our company deals in Machine Tools & Accessories, you will find out more about us in our web site www.valtorin.com.sg

Valtorin Tools is the distributor, so its logo should be the most prominent followed by the rest of the product logos.

Target Market(s)

Mechanical Engineers

Industry/Entity Type

It Company

Requirements
Must have
• It should not take my customers too long to open the email.

Nice to have
• It will be nice if its humorous.

It would be nice to see moving graphics.

```html
<!DOCTYPE html>
<html lang="en">
<head>
<meta charset="utf-8">
<title>Season's Greetings – Valtorin Tools</title>
<link href="https://fonts.googleapis.com/css2?family=Pinyon+Script&family=Montserrat:wght@700&display=swap" rel="stylesheet">
<style>
  :root {
    --card-white: #ffffff;
    --red-deep: #7e0d12;
    --red-mid: #a3161c;
    --red-glow: #c33a36;
    --greeting-pink: #f6dcd4;
    --brand-red: #9c1f2e;
    --ink-dark: #1d2a4a;
  }
  * { margin: 0; padding: 0; box-sizing: border-box; }
  html, body { width: 1200px; height: 808px; overflow: hidden; background: var(--card-white); }
  .card { position: relative; width: 1200px; height: 808px; background: var(--card-white); }
  .festive-scene { position: absolute; left: 0; top: 0; width: 1200px; height: 650px; }
  .greeting { position: absolute; font-family: "Pinyon Script", cursive; color: var(--greeting-pink);
    text-shadow: 0 2px 4px rgba(60, 0, 0, .45); white-space: nowrap; line-height: 1; }
  .greeting--seasons { left: 248px; top: 200px; font-size: 74px; }
  .greeting--and { left: 420px; top: 294px; font-size: 48px; }
  .greeting--new-year { left: 436px; top: 362px; font-size: 82px; }
  .partner-brands { position: absolute; left: 88px; top: 672px; width: 690px;
    display: grid; grid-template-columns: repeat(5, 1fr); row-gap: 22px; column-gap: 10px; }
  .partner-brand { height: 40px; display: flex; align-items: center; justify-content: center;
    font-family: "Montserrat", sans-serif; font-weight: 700; font-size: 17px; letter-spacing: .5px; }
  .partner-brand--red { color: #c8202a; }
  .partner-brand--blue { color: #1f4f9a; }
  .partner-brand--orange { color: #e07a12; }
  .partner-brand--navy { color: var(--ink-dark); }
  .partner-brand--green { color: #2b8a3e; }
  .distributor { position: absolute; left: 818px; top: 690px; display: flex; align-items: center; gap: 16px; }
  .distributor__mark { width: 34px; height: 34px; border-radius: 50%; background: var(--brand-red); }
  .distributor__name { font-family: "Montserrat", sans-serif; font-weight: 700; font-size: 38px;
    color: var(--brand-red); letter-spacing: 1px; }
</style>
</head>
<body>
<main class="card">
  <svg class="festive-scene" viewBox="0 0 1200 650" role="img" aria-label="Deep red festive panel framed by drifting white snowflakes, with a row of snowy pine trees along the bottom">
    <defs>
      <radialGradient id="panel-glow" cx="50%" cy="42%" r="62%">
        <stop offset="0" stop-color="var(--red-glow)"/>
        <stop offset=".55" stop-color="var(--red-mid)"/>
        <stop offset="1" stop-color="var(--red-deep)"/>
      </radialGradient>
      <radialGradient id="frost-edge" cx="50%" cy="48%" r="60%">
        <stop offset=".72" stop-color="#fff" stop-opacity="0"/>
        <stop offset=".9" stop-color="#fff" stop-opacity=".75"/>
        <stop offset="1" stop-color="#fff" stop-opacity="1"/>
      </radialGradient>
      <linearGradient id="snow-ground" x1="0" y1="0" x2="0" y2="1">
        <stop offset="0" stop-color="#fff" stop-opacity="0"/>
        <stop offset=".6" stop-color="#fff" stop-opacity=".85"/>
        <stop offset="1" stop-color="#fff"/>
      </linearGradient>
    </defs>
    <rect width="1200" height="650" fill="url(#panel-glow)"/>
    <rect width="1200" height="650" fill="url(#frost-edge)"/>
    <rect y="450" width="1200" height="200" fill="url(#snow-ground)"/>
  </svg>

  <p class="greeting greeting--seasons">Season's Greetings</p>
  <p class="greeting greeting--and">and...</p>
  <p class="greeting greeting--new-year">Happy New Year!</p>

  <ul class="partner-brands" aria-label="Product brands">
    <li class="partner-brand partner-brand--red">Brisca</li>
    <li class="partner-brand partner-brand--blue">Rolvane</li>
    <li class="partner-brand partner-brand--orange">Teskor Hallen</li>
    <li class="partner-brand partner-brand--navy">Grivo</li>
    <li class="partner-brand partner-brand--orange">Flexa-Run</li>
    <li class="partner-brand partner-brand--blue">Dornmet</li>
    <li class="partner-brand partner-brand--navy">Kello</li>
    <li class="partner-brand partner-brand--blue">Vesterle</li>
    <li class="partner-brand partner-brand--green">Mossleaf</li>
    <li class="partner-brand partner-brand--blue">Brandhal</li>
  </ul>

  <div class="distributor">
    <span class="distributor__mark" aria-hidden="true"></span>
    <span class="distributor__name">Valtorin Tools</span>
  </div>
</main>
</body>
</html>
```